Open Gate Chapel Outreach & 99.5 FM & 95.5 FM Radio

One side to be Open Gate Outreach logo (under design now) with Torvo & Maribel Quenstad contact info.

The other side to show Torvo Quenstad info and;

99.5 FM The LAMP
M-F 9:30pm-10:00pm
for the Broken, Lost & incarcerated

95.5 FM The DOVE
M-F 5:00am-9:00am
Hawaii's only LIVE Christian Radio Program
Fun for the whole family!

Radio logos can be taken from websites

Industry/Entity Type

Radio

```html
<!DOCTYPE html>
<html lang="en">
<head>
<meta charset="utf-8">
<title>Open Gate Outreach – Business Cards</title>
<link rel="stylesheet" href="https://fonts.googleapis.com/css2?family=Open+Sans:wght@400;600&display=swap">
<style>
  :root {
    --page-bg: #d9d9d9;
    --card-bg: #ffffff;
    --accent-red: #a8232b;
    --accent-blue: #2aa3d6;
    --panel-grey: #e8e8e8;
    --text-navy: #1f3f78;
    --text-dark: #333333;
  }
  * { margin: 0; padding: 0; box-sizing: border-box; }
  html, body {
    width: 1200px; height: 1200px; overflow: hidden;
    background: var(--page-bg);
    font-family: "Open Sans", sans-serif;
  }
  .sheet { position: relative; width: 1200px; height: 1200px; }
  .card {
    position: absolute; left: 150px; width: 900px; height: 514px;
    background: var(--card-bg);
    box-shadow: 0 6px 20px rgba(0,0,0,0.18);
    overflow: hidden;
  }
  .card--back { top: 70px; }
  .card--front { top: 616px; }
  .card svg.card-shapes { position: absolute; inset: 0; }
  .txt { position: absolute; white-space: nowrap; }

  /* back side */
  .back-name { left: 42px; top: 30px; font-size: 26px; color: var(--accent-red); font-variant: small-caps; letter-spacing: 0.5px; }
  .back-line { left: 42px; font-size: 18px; color: var(--text-dark); }
  .back-line--call { top: 72px; }
  .back-line--web { top: 100px; }
  .station-title { font-size: 24px; line-height: 1.3; color: var(--text-navy); }
  .station-detail { font-size: 17px; line-height: 1.35; color: var(--text-dark); }
  .station--lamp { left: 190px; top: 180px; }
  .station--dove { right: 160px; top: 326px; text-align: right; }
  .station-mark {
    position: absolute; font-size: 17px; font-weight: 600; color: var(--text-navy);
    display: flex; align-items: center; gap: 6px; white-space: nowrap;
  }
  .station-mark--lamp { left: 24px; top: 222px; }
  .station-mark--dove { right: 22px; top: 382px; }
  .mark-dot { width: 12px; height: 12px; background: var(--accent-red); border-radius: 50%; }

  /* front side */
  .front-name { left: 44px; top: 288px; font-size: 34px; line-height: 1.3; color: var(--accent-red); }
  .front-phone { left: 90px; top: 370px; font-size: 21px; color: var(--text-dark); }
  .front-web { left: 566px; top: 452px; font-size: 20px; color: var(--text-dark); }
  .icon { position: absolute; }
</style>
</head>
<body>
<main class="sheet">

  <!-- Back: radio programs -->
  <section class="card card--back" aria-label="Card back, radio programs">
    <svg class="card-shapes" width="900" height="514" viewBox="0 0 900 514" aria-hidden="true">
      <line x1="250" y1="50" x2="880" y2="50" stroke="var(--accent-blue)" stroke-width="3"/>
      <line x1="0" y1="150" x2="900" y2="150" stroke="var(--accent-red)" stroke-width="3"/>
      <polygon points="0,165 480,165 440,300 0,300" fill="var(--panel-grey)"/>
      <polygon points="500,315 900,315 900,480 455,480" fill="var(--panel-grey)"/>
    </svg>

    <div class="txt back-name">Torvo Quenstad</div>
    <div class="txt back-line back-line--call">Call -555-0142</div>
    <div class="txt back-line back-line--web">web -hawaii.opengateoutreach.org</div>

    <div class="station-mark station-mark--lamp"><span class="mark-dot"></span>99.5 The LAMP</div>
    <div class="txt station--lamp">
      <div class="station-title">99.5 FM The LAMP</div>
      <div class="station-detail">M-F 9:30pm-10:00pm<br>for the Broken,<br>Lost &amp; incarcerated</div>
    </div>

    <div class="txt station--dove">
      <div class="station-title">95.5 FM The DOVE</div>
      <div class="station-detail">M-F 5:00am-9:00am<br>Hawaii's only LIVE<br>Christian Radio Program<br>Fun for the whole family!</div>
    </div>
    <div class="station-mark station-mark--dove">95.5 The DOVE</div>
  </section>

  <!-- Front: contact -->
  <section class="card card--front" aria-label="Card front, contact details">
    <svg class="card-shapes" width="900" height="514" viewBox="0 0 900 514" aria-hidden="true">
      <polygon points="30,352 418,352 460,420 30,420" fill="var(--panel-grey)"/>
      <polygon points="520,436 880,436 880,496 520,496" fill="var(--panel-grey)"/>
      <polyline points="30,342 440,342 490,422 880,422" fill="none" stroke="var(--accent-blue)" stroke-width="3"/>
    </svg>

    <div class="txt front-name">Torvo &amp; Maribel Quenstad</div>

    <svg class="icon" style="left:50px;top:370px" width="28" height="28" viewBox="0 0 28 28" aria-hidden="true">
      <circle cx="14" cy="14" r="12" fill="none" stroke="var(--accent-blue)" stroke-width="2"/>
      <path d="M10 8 l3 0 l1 4 l-2 1 q1 3 3 4 l1 -2 l4 1 l0 3 q-8 1 -10 -11z" fill="var(--accent-blue)"/>
    </svg>
    <div class="txt front-phone">555-0142</div>

    <svg class="icon" style="left:530px;top:451px" width="30" height="30" viewBox="0 0 30 30" aria-hidden="true">
      <circle cx="15" cy="15" r="13" fill="none" stroke="var(--accent-blue)" stroke-width="2"/>
      <circle cx="15" cy="15" r="8" fill="none" stroke="var(--accent-blue)" stroke-width="1.5"/>
      <ellipse cx="15" cy="15" rx="3.5" ry="8" fill="none" stroke="var(--accent-blue)" stroke-width="1.3"/>
      <line x1="7" y1="15" x2="23" y2="15" stroke="var(--accent-blue)" stroke-width="1.3"/>
    </svg>
    <div class="txt front-web">hawaii.opengateoutreach.org</div>
  </section>

</main>
</body>
</html>
```